Online media outlet needs a blog and logo

A new online blog platform is being established in the UK. The blog will be very similar in layout to www.lumvero.co. It will need to have a main story slider showing three slides and block tiles beneath the slider for additional tiles.

The blog platform will be called 'Brisket Lantern' and will also need a professional looking logo design for the name.

The website should be designed in Word Press.

Industry/Entity Type

Media

Logo Text

Brisket Lantern

Coding

Coded - Design and coding required

Number of Pages Required

3 page

Font styles to use
Other font styles liked:
• Helvetica

Requirements
Must have
• A slider showing three slides. Be similar to Lum V (see previous comment). Be Word Press compatible.

```html
<!DOCTYPE html>
<html lang="en">
<head>
<meta charset="utf-8">
<title>Brisket Lantern</title>
<link rel="stylesheet" href="https://fonts.googleapis.com/css2?family=Open+Sans:wght@400;600;700;800&display=swap">
<style>
  :root {
    --navy: #1b2a45;
    --navy-deep: #15223a;
    --rust: #b4542a;
    --ink: #1a1a1a;
    --body: #222;
    --white: #ffffff;
    --footer: #000000;
    --footer-text: #e8e8e8;
  }
  * { box-sizing: border-box; margin: 0; padding: 0; }
  html, body { width: 1200px; height: 2528px; overflow: hidden; }
  body { position: relative; background: var(--white); font-family: "Open Sans", Arial, sans-serif; color: var(--body); }

  .site-header { position: absolute; left: 0; top: 0; width: 1200px; height: 111px; background: var(--navy); color: var(--white); }
  .locale { position: absolute; left: 54px; top: 40px; font-size: 22px; }
  .locale svg { vertical-align: middle; margin-left: 4px; }
  .brand { position: absolute; left: 0; width: 1200px; top: 36px; text-align: center; font-size: 30px; font-weight: 700; letter-spacing: 1px; }
  .search { position: absolute; left: 800px; top: 40px; width: 253px; height: 31px; background: var(--white); }
  .search svg { position: absolute; right: 12px; top: 3px; }
  .menu-toggle { position: absolute; left: 1095px; top: 44px; }

  .hero { position: absolute; left: 0; top: 111px; width: 1200px; height: 800px;
    background: linear-gradient(180deg, #a77a5c 0%, #c98e62 14%, #b9734a 26%, #a4502d 38%, #8a4a2c 48%, #7a6b4e 56%, #5d5c55 66%, #4d4d4d 80%, #454545 100%); }
  .main-nav { position: absolute; left: 0; top: 20px; width: 1200px; height: 39px; background: var(--navy-deep); display: flex; justify-content: center; align-items: center; gap: 35px; }
  .main-nav a { color: var(--white); text-decoration: none; font-size: 12px; font-weight: 700; }
  .hero-title { position: absolute; left: 0; width: 1200px; top: 142px; text-align: center; color: var(--white); font-size: 70px; font-weight: 800; letter-spacing: 1px; }
  .hero-tag { position: absolute; left: 492px; top: 233px; width: 216px; height: 55px; background: var(--navy); color: var(--white); font-size: 24px; font-weight: 700; display: flex; align-items: center; justify-content: center; }

  .tiles { position: absolute; left: 64px; width: 1072px; display: grid; grid-template-columns: repeat(3, 337px); column-gap: 30px; }
  .tiles.row-1 { top: 741px; }
  .tiles.row-2 { top: 1473px; }
  .tile { text-align: center; }
  .tile-photo { height: 223px; }
  .photo-phone { background: linear-gradient(135deg, #b8231f 0%, #d62b25 45%, #8f1c19 70%, #dcdfe4 100%); }
  .photo-car { background: linear-gradient(180deg, #7a7c62 0%, #3f5a2c 35%, #5f8a36 55%, #b0412f 70%, #c8b393 100%); }
  .photo-aurora { background: linear-gradient(160deg, #7fe3c4 0%, #3f9f8c 25%, #1d2f5e 55%, #2a1f4e 80%, #e7e4f2 100%); }
  .tile-title { margin-top: 44px; color: var(--rust); font-size: 28px; font-weight: 700; }
  .tile-subtitle { margin-top: 6px; font-size: 21px; color: var(--ink); }
  .tile-text { margin: 14px auto 0; width: 300px; font-size: 16px; line-height: 27px; color: var(--ink); }
  .read-more { display: flex; align-items: center; justify-content: center; margin: 47px auto 0; width: 175px; height: 39px; background: var(--rust); color: var(--white); font-size: 16px; font-weight: 600; text-decoration: none; }

  .site-footer { position: absolute; left: 0; top: 2209px; width: 1200px; height: 319px; background: var(--footer); color: var(--footer-text); }
  .footer-col { position: absolute; top: 40px; font-size: 17px; line-height: 25px; }
  .footer-col h3 { font-size: 22px; font-weight: 700; color: var(--white); margin-bottom: 10px; line-height: 28px; }
  .footer-col p { margin: 0; }
  .footer-col .gap { margin-top: 5px; }
  .social { display: flex; align-items: center; gap: 6px; margin-bottom: 4px; }
  .social i { display: inline-block; width: 21px; height: 21px; border-radius: 50%; background: var(--rust); }
  .copyright { margin-top: 20px; }
</style>
</head>
<body>
  <header class="site-header">
    <div class="locale">United Kingdom &nbsp;|&nbsp; English
      <svg width="14" height="10" viewBox="0 0 14 10"><path d="M2 2 L7 7 L12 2" fill="none" stroke="#fff" stroke-width="2"/></svg>
    </div>
    <div class="brand">BRISKET LANTERN</div>
    <div class="search">
      <svg width="26" height="26" viewBox="0 0 26 26"><circle cx="14" cy="12" r="7" fill="none" stroke="#1b2a45" stroke-width="3"/><path d="M9 17 L4 22" stroke="#1b2a45" stroke-width="3"/></svg>
    </div>
    <svg class="menu-toggle" width="51" height="24" viewBox="0 0 51 24"><rect y="0" width="51" height="4" fill="#fff"/><rect y="10" width="51" height="4" fill="#fff"/><rect y="20" width="51" height="4" fill="#fff"/></svg>
  </header>

  <section class="hero" role="img" aria-label="Desert road winding through red rock canyons under an amber sky">
    <nav class="main-nav">
      <a href="#">HOME</a><a href="#">EDITORIAL</a><a href="#">WORLD</a><a href="#">POLITICS</a><a href="#">TECHNOLOGY</a><a href="#">ART</a>
    </nav>
    <h1 class="hero-title">HEATED DISCUSSION</h1>
    <div class="hero-tag">TOP STORY</div>
  </section>

  <section class="tiles row-1">
    <article class="tile">
      <div class="tile-photo photo-phone" role="img" aria-label="Red telephone box seen from below"></div>
      <h2 class="tile-title">TITLE GOES HERE</h2>
      <p class="tile-subtitle">Subtitle goes here</p>
      <p class="tile-text">Lorem ipsum dolor sit amet, consectetuer adipiscing elit, sed diam nonummy nibh euismod tincidunt ut laoreet dolore magna aliquam erat volutpat. Ut wisi enim ad minim veniam, quis nostrud exerci.</p>
      <a class="read-more" href="#">Read more</a>
    </article>
    <article class="tile">
      <div class="tile-photo photo-car" role="img" aria-label="Vintage red convertible on a dirt road lined with trees"></div>
      <h2 class="tile-title">TITLE GOES HERE</h2>
      <p class="tile-subtitle">Subtitle goes here</p>
      <p class="tile-text">Lorem ipsum dolor sit amet, consectetuer adipiscing elit, sed diam nonummy nibh euismod tincidunt ut laoreet dolore magna aliquam erat volutpat. Ut wisi enim ad minim veniam, quis nostrud exerci.</p>
      <a class="read-more" href="#">Read more</a>
    </article>
    <article class="tile">
      <div class="tile-photo photo-aurora" role="img" aria-label="Green northern lights over a snowy plain at night"></div>
      <h2 class="tile-title">TITLE GOES HERE</h2>
      <p class="tile-subtitle">Subtitle goes here</p>
      <p class="tile-text">Lorem ipsum dolor sit amet, consectetuer adipiscing elit, sed diam nonummy nibh euismod tincidunt ut laoreet dolore magna aliquam erat volutpat. Ut wisi enim ad minim veniam, quis nostrud exerci.</p>
      <a class="read-more" href="#">Read more</a>
    </article>
  </section>

  <section class="tiles row-2">
    <article class="tile">
      <div class="tile-photo photo-car" role="img" aria-label="Vintage red convertible on a dirt road lined with trees"></div>
      <h2 class="tile-title">TITLE GOES HERE</h2>
      <p class="tile-subtitle">Subtitle goes here</p>
      <p class="tile-text">Lorem ipsum dolor sit amet, consectetuer adipiscing elit, sed diam nonummy nibh euismod tincidunt ut laoreet dolore magna aliquam erat volutpat. Ut wisi enim ad minim veniam, quis nostrud exerci.</p>
      <a class="read-more" href="#">Read more</a>
    </article>
    <article class="tile">
      <div class="tile-photo photo-aurora" role="img" aria-label="Green northern lights over a snowy plain at night"></div>
      <h2 class="tile-title">TITLE GOES HERE</h2>
      <p class="tile-subtitle">Subtitle goes here</p>
      <p class="tile-text">Lorem ipsum dolor sit amet, consectetuer adipiscing elit, sed diam nonummy nibh euismod tincidunt ut laoreet dolore magna aliquam erat volutpat. Ut wisi enim ad minim veniam, quis nostrud exerci.</p>
      <a class="read-more" href="#">Read more</a>
    </article>
    <article class="tile">
      <div class="tile-photo photo-phone" role="img" aria-label="Red telephone box seen from below"></div>
      <h2 class="tile-title">TITLE GOES HERE</h2>
      <p class="tile-subtitle">Subtitle goes here</p>
      <p class="tile-text">Lorem ipsum dolor sit amet, consectetuer adipiscing elit, sed diam nonummy nibh euismod tincidunt ut laoreet dolore magna aliquam erat volutpat. Ut wisi enim ad minim veniam, quis nostrud exerci.</p>
      <a class="read-more" href="#">Read more</a>
    </article>
  </section>

  <footer class="site-footer">
    <div class="footer-col" style="left:194px">
      <h3>Follow Us</h3>
      <p class="social"><i></i>Like us on Hubbly</p>
      <p class="social"><i></i>Follow us on Chirpo</p>
      <p class="social"><i></i>Follow us on Pinfolio</p>
      <p class="copyright">© by &nbsp;COMPANYNAME</p>
    </div>
    <div class="footer-col" style="left:440px">
      <h3>Address</h3>
      <p>Company Name</p><p>01234567</p><p>email@example.com</p><p class="gap">www.url.com</p><p>Street, City, ZIP</p>
    </div>
    <div class="footer-col" style="left:645px">
      <h3>Address</h3>
      <p>Company Name</p><p>01234567</p><p>email@example.com</p><p class="gap">www.url.com</p><p>Street, City, ZIP</p>
    </div>
    <div class="footer-col" style="left:851px">
      <h3>Address</h3>
      <p>Company Name</p><p>01234567</p><p>email@example.com</p><p class="gap">www.url.com</p><p>Street, City, ZIP</p>
    </div>
  </footer>
</body>
</html>
```